qlxcard
business card
qlxcard - Retailers
Creative Brief
Bright & Fun-filled
Dennis Halvorsen
General Manager
38146 Quarry Lane Harlow Twp., MN. 48297
dennis@lakeshorepanelcrafters.example
www.lakeshorepanelcrafters.example
We are custom frame designers located in Harlow Twp., MN. We specialize in career presentations for all public and private occupations. Framing presentations include retirement, recognition, awards, certificates and uniform display.
We also provide framed items and silent auction services for all your fund raising and charity needs. Our silent auction service is a great way to raise money at no cost to the charity and provide your attendees with the opportunity to win some great items.
Concepts
Business Card for Womens Clothing Boutique

```html
<!DOCTYPE html>
<html lang="en">
<head>
<meta charset="utf-8">
<title>qlxcard – business card options</title>
<link rel="stylesheet" href="https://fonts.googleapis.com/css2?family=Cinzel:wght@400;700&family=Open+Sans:wght@700&display=swap">
<style>
  :root{
    --stage-top:#f4f4f4;
    --stage-bottom:#d9d9d9;
    --ink-black:#050608;
    --navy:#06203f;
    --blue:#0d63b0;
    --blue-bright:#1d8be0;
    --text-light:#e8eef6;
    --text-dim:#b9c8d8;
    --label:#1b1b1b;
  }
  *{box-sizing:border-box;margin:0;padding:0}
  html,body{width:1200px;height:901px;overflow:hidden}
  body{
    position:relative;
    background:radial-gradient(ellipse at 50% 40%,var(--stage-top),var(--stage-bottom));
    font-family:'Cinzel',serif;
    color:var(--text-light);
  }
  .card{position:absolute;width:560px;overflow:hidden;box-shadow:0 4px 10px rgba(0,0,0,.35)}
  .card--front{height:341px;top:68px}
  .card--back{height:317px;top:438px}
  .opt1{left:24px}
  .opt2{left:616px}

  .opt1.card--front{background:linear-gradient(90deg,var(--ink-black) 0 138px,var(--navy) 138px,var(--blue) 60%,var(--blue-bright))}
  .opt2.card--front{background:linear-gradient(135deg,var(--navy),var(--blue) 55%,var(--blue-bright))}
  .opt1.card--back{background:linear-gradient(90deg,var(--ink-black) 0 120px,var(--navy) 127px,var(--blue-bright) 150px,var(--navy) 175px,var(--ink-black) 185px)}
  .opt2.card--back{background:linear-gradient(180deg,var(--navy),var(--blue) 45%,var(--navy) 80%)}

  .brand{position:absolute;border-radius:50%;background:var(--navy);border:3px solid var(--text-light);
    display:flex;align-items:center;justify-content:center;text-align:center;
    font-size:11px;line-height:1.3;color:var(--text-light);padding:14px}
  .ghost-ring{position:absolute;border-radius:50%;border:2px solid rgba(255,255,255,.09);background:rgba(255,255,255,.04)}

  .person{position:absolute;left:170px;top:100px}
  .opt2 .person{left:163px}
  .person__name{font-size:20px;letter-spacing:.5px}
  .person__role{font-size:12px;color:var(--text-dim);margin-top:2px}

  .contact{position:absolute;left:195px;top:212px;list-style:none}
  .opt2 .contact{left:188px}
  .contact li{display:flex;align-items:center;gap:8px;font-size:12.5px;height:22px;white-space:nowrap}
  .contact svg{width:13px;height:13px;flex:none}

  .tagline{position:absolute;font-size:16px;line-height:1.35}
  .opt1 .tagline{left:207px;top:32px;font-size:14px;width:330px}
  .opt2 .tagline{left:58px;top:32px;width:460px;font-size:18px}

  .services{position:absolute;list-style:none;font-size:13px}
  .opt1 .services{left:268px;top:128px}
  .opt1 .services li{height:34px}
  .opt2 .services{left:107px;top:100px;font-size:14px}
  .opt2 .services li{height:29px}
  .services li{display:flex;align-items:center;gap:12px}
  .services svg{width:10px;height:10px}

  .footer-band{position:absolute;left:0;right:0;bottom:0;height:62px;background:var(--ink-black);border-top:2px solid var(--blue-bright);
    font-size:12px;padding:20px 0 0 78px}

  .option-label{position:absolute;top:780px;width:300px;text-align:center;font-family:'Open Sans',sans-serif;font-weight:700;font-size:40px;color:var(--label)}
</style>
</head>
<body>

<section class="card card--front opt1">
  <div class="brand" style="left:20px;top:25px;width:120px;height:120px">Lakeshore Panel Crafters</div>
  <div class="person"><p class="person__name">Dennis Halvorsen</p><p class="person__role">General Manager</p></div>
  <ul class="contact">
    <li><svg viewBox="0 0 12 12"><path d="M1 6 6 1.5 11 6v5H1z" fill="#fff"/></svg>38146 Quarry Lane, Harlow Twp., MN. 48297</li>
    <li><svg viewBox="0 0 12 12"><circle cx="6" cy="6" r="5" fill="none" stroke="#fff" stroke-width="1.6"/></svg>dennis@lakeshorepanelcrafters.example</li>
    <li><svg viewBox="0 0 12 12"><circle cx="6" cy="6" r="5" fill="#fff"/></svg>www.lakeshorepanelcrafters.example</li>
    <li><svg viewBox="0 0 12 12"><rect width="12" height="12" rx="2" fill="#3a64b0"/></svg>@lakeshorepanelcrafters</li>
    <li><svg viewBox="0 0 12 12"><rect width="12" height="12" rx="2" fill="#3fb6e8"/></svg>@lakeshorepanelcrafters</li>
  </ul>
</section>

<section class="card card--front opt2">
  <div class="ghost-ring" style="left:380px;top:-20px;width:220px;height:220px"></div>
  <div class="person"><p class="person__name">Dennis Halvorsen</p><p class="person__role">General Manager</p></div>
  <ul class="contact">
    <li><svg viewBox="0 0 12 12"><path d="M1 6 6 1.5 11 6v5H1z" fill="#fff"/></svg>38146 Quarry Lane, Harlow Twp., MN. 48297</li>
    <li><svg viewBox="0 0 12 12"><circle cx="6" cy="6" r="5" fill="none" stroke="#fff" stroke-width="1.6"/></svg>dennis@lakeshorepanelcrafters.example</li>
    <li><svg viewBox="0 0 12 12"><circle cx="6" cy="6" r="5" fill="#fff"/></svg>www.lakeshorepanelcrafters.example</li>
    <li><svg viewBox="0 0 12 12"><rect width="12" height="12" rx="2" fill="#3a64b0"/></svg>@lakeshorepanelcrafters</li>
    <li><svg viewBox="0 0 12 12"><rect width="12" height="12" rx="2" fill="#3fb6e8"/></svg>@lakeshorepanelcrafters</li>
  </ul>
</section>

<section class="card card--back opt1">
  <div class="brand" style="left:25px;top:127px;width:110px;height:110px;font-size:10px">Lakeshore Panel Crafters</div>
  <p class="tagline">Custom framed career presentations for all public and private occupations.</p>
  <ul class="services">
    <li><svg viewBox="0 0 10 10"><path d="M5 0 10 5 5 10 0 5z" fill="#fff"/></svg>Retirement</li>
    <li><svg viewBox="0 0 10 10"><path d="M5 0 10 5 5 10 0 5z" fill="#fff"/></svg>Recognition</li>
    <li><svg viewBox="0 0 10 10"><path d="M5 0 10 5 5 10 0 5z" fill="#fff"/></svg>Certificates</li>
    <li><svg viewBox="0 0 10 10"><path d="M5 0 10 5 5 10 0 5z" fill="#fff"/></svg>Awards</li>
    <li><svg viewBox="0 0 10 10"><path d="M5 0 10 5 5 10 0 5z" fill="#fff"/></svg>Uniform Displays</li>
  </ul>
</section>

<section class="card card--back opt2">
  <p class="tagline">Custom framed career presentations for all public and private occupations.</p>
  <ul class="services">
    <li><svg viewBox="0 0 10 10"><path d="M5 0 6.2 3.6 10 3.8 7 6.1 8.1 10 5 7.8 1.9 10 3 6.1 0 3.8 3.8 3.6z" fill="#fff"/></svg>Retirement</li>
    <li><svg viewBox="0 0 10 10"><path d="M5 0 6.2 3.6 10 3.8 7 6.1 8.1 10 5 7.8 1.9 10 3 6.1 0 3.8 3.8 3.6z" fill="#fff"/></svg>Recognition</li>
    <li><svg viewBox="0 0 10 10"><path d="M5 0 6.2 3.6 10 3.8 7 6.1 8.1 10 5 7.8 1.9 10 3 6.1 0 3.8 3.8 3.6z" fill="#fff"/></svg>Certificates</li>
    <li><svg viewBox="0 0 10 10"><path d="M5 0 6.2 3.6 10 3.8 7 6.1 8.1 10 5 7.8 1.9 10 3 6.1 0 3.8 3.8 3.6z" fill="#fff"/></svg>Awards</li>
    <li><svg viewBox="0 0 10 10"><path d="M5 0 6.2 3.6 10 3.8 7 6.1 8.1 10 5 7.8 1.9 10 3 6.1 0 3.8 3.8 3.6z" fill="#fff"/></svg>Uniform Displays</li>
  </ul>
  <div class="footer-band">www.lakeshorepanelcrafters.example</div>
  <div class="brand" style="left:410px;top:185px;width:106px;height:106px;font-size:10px">Lakeshore Panel Crafters</div>
</section>

<p class="option-label" style="left:154px">Option 1</p>
<p class="option-label" style="left:746px">Option 2</p>

</body>
</html>
```